Pull Up Banner Design 85cm X200cm

The pull up banner is intended for branding and services awareness purposes, and to be used at exhibition and conference. Please refer to the websites below for more information
1. https://www.advisory-nook.net/
2. https://www.advisory-nook.net/landing-page
3. https://blog.advisory-nook.net/faq-for-client/
4. https://blog.advisory-nook.net/faq-for-advisor/

Ideally, the banner will lead potential users both young entrepreneurs and online business owners (as clients) to Brivana Hub marketplace, and also professional services providers like accountants and finance advisors and consultants (as advisors) to sign up with the platform. (Like ArtForge marketplace)

Target Market(s)

Business users and accountants aged between 25 to 44 yrs old

Requirements
Must have
• website address (www.advisory-nook.net)
• and
• company logo "Brivana Hub" as attached

```html
<!DOCTYPE html>
<html lang="en">
<head>
<meta charset="utf-8">
<title>Brivana Hub – Pull Up Banner</title>
<link href="https://fonts.googleapis.com/css2?family=Bebas+Neue&family=Montserrat:wght@600&family=Roboto:wght@300;400&display=swap" rel="stylesheet">
<style>
  :root {
    --stage: #e4e4e4;
    --paper: #f1f2f4;
    --brand-blue: #1474c4;
    --slate: #58595b;
    --ink: #3c3c3c;
    --body: #4a4a4a;
    --white: #ffffff;
    --rule: #c9cbcf;
    --teal: #6fc9c3;
  }
  * { margin: 0; padding: 0; box-sizing: border-box; }
  html, body { width: 1200px; height: 1050px; overflow: hidden; background: var(--stage); }
  .banner {
    position: absolute; left: 386px; top: 25px; width: 428px; height: 1000px;
    background: var(--paper); overflow: hidden;
    font-family: "Roboto", Arial, sans-serif;
    box-shadow: 0 6px 18px rgba(0,0,0,.18);
  }
  .banner-shapes { position: absolute; inset: 0; }
  .headline {
    position: absolute; left: 20px; top: 66px;
    font-family: "Bebas Neue", Impact, sans-serif; font-weight: 400; color: var(--white);
    font-size: 38px; line-height: 42px; letter-spacing: .5px;
    text-shadow: 0 1px 3px rgba(0,0,0,.3);
  }
  .brand-mark {
    position: absolute; left: 166px; top: 281px; width: 92px; height: 92px;
    border-radius: 50%; background: var(--brand-blue); border: 6px solid var(--white);
  }
  .brand-name {
    position: absolute; left: 0; width: 100%; top: 364px; text-align: center;
    font-family: "Montserrat", Arial, sans-serif; font-weight: 600;
    font-size: 38px; color: var(--brand-blue);
  }
  .tagline {
    position: absolute; left: 0; width: 100%; top: 430px; text-align: center;
    font-weight: 300; font-size: 20px; color: var(--ink);
  }
  .section-tab { position: absolute; font-size: 18px; color: var(--white); font-weight: 400; }
  .tab-clients { left: 18px; top: 484px; }
  .tab-advisors { left: 222px; top: 694px; }
  .feature { position: absolute; width: 124px; text-align: center; }
  .col-1 { left: 12px; }
  .col-2 { left: 152px; }
  .col-3 { left: 292px; }
  .row-1 { top: 534px; }
  .row-2 { top: 742px; }
  .feature-icon { width: 56px; height: 56px; border-radius: 50%; margin: 0 auto 8px; }
  .icon-teal { background: var(--teal); }
  .icon-ring { background: var(--white); border: 2px solid var(--brand-blue); }
  .feature-title { font-size: 11.5px; line-height: 13px; color: var(--brand-blue); margin-bottom: 6px; white-space: nowrap; }
  .feature-text { font-size: 6px; line-height: 7.5px; color: var(--body); padding: 0 2px; }
  .site-url {
    position: absolute; left: 0; width: 100%; top: 930px; text-align: center;
    font-size: 21px; color: var(--white); letter-spacing: .3px;
  }
  .globe { display: inline-block; vertical-align: -3px; margin-right: 12px; }
</style>
</head>
<body>
<div class="banner">
  <svg class="banner-shapes" width="428" height="1000" viewBox="0 0 428 1000">
    <defs>
      <linearGradient id="photoTone" x1="0" y1="0" x2="1" y2="1">
        <stop offset="0" stop-color="#4b4a4c"/>
        <stop offset=".45" stop-color="#7a6a5e"/>
        <stop offset="1" stop-color="#b79e86"/>
      </linearGradient>
    </defs>
    <g role="img" aria-label="Photo of a smiling young woman with curly hair looking at her smartphone">
      <path d="M0 0 H428 V322 Q214 372 0 322 Z" fill="url(#photoTone)"/>
    </g>
    <path d="M0 322 Q214 372 428 322" fill="none" stroke="var(--rule)" stroke-width="5"/>
    <path d="M0 479 H256 L266 511 H0 Z" fill="var(--brand-blue)"/>
    <path d="M172 690 H428 V722 H166 Z" fill="var(--slate)"/>
    <path d="M0 892 Q214 848 428 892 V1000 H0 Z" fill="var(--rule)"/>
    <path d="M0 898 Q214 856 428 898 V1000 H0 Z" fill="var(--brand-blue)"/>
  </svg>

  <h1 class="headline">Brivana Hub<br>matches you with<br>the right advisors<br>online!</h1>

  <div class="brand-mark"></div>
  <div class="brand-name">Brivana Hub</div>
  <p class="tagline">We’ll Find the Best Advisors for You!</p>

  <div class="section-tab tab-clients">Looking for an advisor?</div>

  <div class="feature col-1 row-1">
    <div class="feature-icon icon-teal" role="img" aria-label="Illustration of an online shop on a computer screen"></div>
    <div class="feature-title">One-stop borderless<br>marketplace</div>
    <div class="feature-text">Access instantly to a network of great independent advisors, consultants, industry professionals, boutique firms and small sized practices, including best talents in accounting, finance and strategy all in one place.</div>
  </div>
  <div class="feature col-2 row-1">
    <div class="feature-icon icon-teal" role="img" aria-label="Illustration of a running figure"></div>
    <div class="feature-title">Convenient and<br>quick</div>
    <div class="feature-text">Get matched instantly to 3 of the great advisors for you to compare. Then communicate, chat, interview, appoint and sign the engagement online.</div>
  </div>
  <div class="feature col-3 row-1">
    <div class="feature-icon icon-teal" role="img" aria-label="Illustration of a thumbs-up hand"></div>
    <div class="feature-title">Hire with<br>confidence</div>
    <div class="feature-text">Explore each advisors profile and browse their previous works as well as clients review in a simple manner online.</div>
  </div>

  <div class="section-tab tab-advisors">Looking for a project?</div>

  <div class="feature col-1 row-2">
    <div class="feature-icon icon-ring" role="img" aria-label="Illustration of a profile card"></div>
    <div class="feature-title">ProfessionalProfile</div>
    <div class="feature-text">Let thousands of line users view<br>your profile every month.</div>
  </div>
  <div class="feature col-2 row-2">
    <div class="feature-icon icon-ring" role="img" aria-label="Illustration of certificates and awards"></div>
    <div class="feature-title">Expertise Showcase</div>
    <div class="feature-text">Let your succes cases and job credentials to be visible online. Users want to connect with you if you have relevant expertise and walked the path before.</div>
  </div>
  <div class="feature col-3 row-2">
    <div class="feature-icon icon-ring" role="img" aria-label="Illustration of a job leads button"></div>
    <div class="feature-title">Job Leads</div>
    <div class="feature-text">You can access to the job<br>leads instantly<br>at the click of the button.</div>
  </div>

  <div class="site-url">
    <svg class="globe" width="20" height="20" viewBox="0 0 20 20" aria-hidden="true">
      <circle cx="10" cy="10" r="8" fill="none" stroke="#fff" stroke-width="2"/>
      <path d="M2 10 H18 M10 2 Q5 10 10 18 M10 2 Q15 10 10 18" fill="none" stroke="#fff" stroke-width="1.5"/>
    </svg>www.advisory-nook.net
  </div>
</div>
</body>
</html>
```